business card deign

Logo needs the following on it.
1. attached logo
2. Tagline - "If it keeps a drink cold or the party going...we do it!"
3. Name- Delia Fenwick, Founder and CPO
4. Address - 418 E. Harlow Avenue, Ste 2204, Tampa, FL. 33719
5. Phone - 720.555.0187

```html
<!DOCTYPE html>
<html lang="en">
<head>
<meta charset="utf-8">
<title>Chillora Business Card</title>
<link href="https://fonts.googleapis.com/css2?family=Montserrat:wght@400;600&display=swap" rel="stylesheet">
<style>
  :root {
    --backdrop: #151515;
    --card: #2b2b2c;
    --ink: #f3f3f3;
    --ink-soft: #e6e6e6;
    --mark: #f3f3f3;
  }
  * { margin: 0; padding: 0; box-sizing: border-box; }
  html, body {
    width: 1200px; height: 1059px; overflow: hidden;
    background: var(--backdrop);
    font-family: "Montserrat", sans-serif;
    color: var(--ink);
  }
  .canvas { position: relative; width: 1200px; height: 1059px; }
  .card {
    position: absolute;
    width: 690px; height: 390px;
    background: var(--card);
    border-radius: 18px;
  }
  .card--front { left: 257px; top: 90px; }
  .card--back { left: 255px; top: 548px; }

  .brand {
    position: absolute;
    display: flex; align-items: center; gap: 12px;
    font-weight: 600;
    color: var(--mark);
    letter-spacing: 0.28em;
    text-transform: uppercase;
  }
  .brand__dot {
    width: 14px; height: 14px; border-radius: 50%;
    background: var(--mark);
    flex: none;
  }
  .card--front .brand { left: 35px; top: 150px; font-size: 26px; }
  .card--back .brand {
    left: 0; right: 0; top: 242px; justify-content: center;
    font-size: 40px;
  }
  .card--back .brand__dot { width: 18px; height: 18px; }

  .person {
    position: absolute; right: 37px; top: 50px; text-align: right;
  }
  .person__name {
    font-weight: 600; font-size: 22px; letter-spacing: 0.04em;
    text-transform: uppercase; line-height: 1.1;
  }
  .person__title {
    font-weight: 400; font-size: 15px; color: var(--ink-soft);
    margin-top: 4px; letter-spacing: 0.02em;
  }

  .contact {
    position: absolute; left: 35px; top: 256px;
    font-size: 15.5px; color: var(--ink-soft); letter-spacing: 0.02em;
  }
  .contact__address { line-height: 22px; }
  .contact__line {
    display: flex; align-items: center; gap: 8px;
    margin-top: 8px; line-height: 18px;
  }
  .contact__address + .contact__line { margin-top: 10px; }
  .contact__icon { width: 12px; height: 12px; fill: var(--ink-soft); flex: none; }

  .tagline {
    position: absolute; left: 0; right: 0; top: 340px;
    text-align: center; font-size: 15px; color: var(--ink-soft);
    letter-spacing: 0.02em;
  }
</style>
</head>
<body>
<main class="canvas">
  <section class="card card--front" aria-label="Card front">
    <div class="brand"><span class="brand__dot"></span>Chillora</div>
    <div class="person">
      <p class="person__name">Delia Fenwick</p>
      <p class="person__title">Founder and CPO</p>
    </div>
    <div class="contact">
      <p class="contact__address">418 E. Harlow Avenue<br>Ste 2204, Tampa, FL. 33719</p>
      <p class="contact__line">
        <svg class="contact__icon" viewBox="0 0 24 24" aria-hidden="true"><path d="M6.6 10.8a15.1 15.1 0 0 0 6.6 6.6l2.2-2.2a1 1 0 0 1 1-.25 11.4 11.4 0 0 0 3.6.57 1 1 0 0 1 1 1V20a1 1 0 0 1-1 1A17 17 0 0 1 3 4a1 1 0 0 1 1-1h3.5a1 1 0 0 1 1 1c0 1.25.2 2.45.57 3.57a1 1 0 0 1-.25 1z"/></svg>
        720.555.0187
      </p>
      <p class="contact__line">
        <svg class="contact__icon" viewBox="0 0 24 24" aria-hidden="true"><path d="M2 5h20v14H2z M4 7v.3l8 5.2 8-5.2V7z" fill-rule="evenodd"/></svg>
        delia@chillora.co
      </p>
    </div>
  </section>

  <section class="card card--back" aria-label="Card back">
    <div class="brand"><span class="brand__dot"></span>Chillora</div>
    <p class="tagline">If it keeps a drink cold or the party going...we do it!</p>
  </section>
</main>
</body>
</html>
```